Banner Ads for Zelvoranet.biz

Hello everyone! We are a online advertising company, and we offer a few unique solutions for advertiser and publishers.
we also buy and sell website traffic!
and for this service we would like to produce some ad banners to promote our offers.
we would like to create the banner in the following formats:
Fullsize Banner 468 x 60
Halfsize Banner 234 x 60
Square Banner 125 x 125
Skyscraper 120 x 600
Bold Skyscraper 160 x 600
Medium Rectangle 300 x 250
Vertical Rectangle 240 x 400
Pop-Up 250 x 250
Industry/Entity Type
Advertising
Requirements
Must have
- catchy design - modern, cool. Maybe Cartoon style
Our ZelvoraNet.biz Logo (only the mascot)
Banners must be animated!

```html
<!DOCTYPE html>
<html lang="en">
<head>
<meta charset="UTF-8">
<title>Zelvoranet.biz – 300x250 Banner Set</title>
<link rel="stylesheet" href="https://fonts.googleapis.com/css2?family=Questrial&family=Open+Sans:wght@400;700&display=swap">
<style>
  :root {
    --stage-bg: #383c3f;
    --stage-text: #e9ebec;
    --banner-red: #a50c06;
    --banner-red-light: #b8150d;
    --banner-red-dark: #6e0603;
    --band-white: #ffffff;
    --band-blush: #ecdcdc;
    --ink: #1c1c1c;
    --headline: #ffffff;
    --chart-white: #f4f4f4;
    --figure-grey: #d9d9d9;
    --mascot-dark: #1f1f22;
    --mascot-mid: #55575c;
    --coin-silver: #c9c9cc;
    --coin-shadow: #8e8e92;
  }
  * { box-sizing: border-box; margin: 0; padding: 0; }
  html, body {
    width: 1200px; height: 900px; overflow: hidden;
    background: var(--stage-bg);
  }
  .board { position: relative; width: 1200px; height: 900px; }
  .format-title {
    position: absolute; left: 0; width: 1200px; top: 192px;
    text-align: center; color: var(--stage-text);
    font: 400 31px/1 "Questrial", sans-serif;
  }
  .banner {
    position: absolute; top: 301px; width: 360px; height: 300px;
    overflow: hidden; border: 1px solid #8a8a8a;
    background: var(--banner-red);
    font-family: "Open Sans", sans-serif;
  }
  .banner-1 { left: 37px; }
  .banner-2 { left: 421px; }
  .banner-3 { left: 810px; }
  .banner-bg { position: absolute; inset: 0; }
  .frame-label {
    position: absolute; width: 200px; margin-left: -100px;
    text-align: center; color: var(--stage-text);
    font: 23px/1 "Questrial", sans-serif;
  }
  .kicker {
    position: absolute; left: 20px; top: 20px;
    color: var(--headline); font: 29px/1 "Questrial", sans-serif;
  }
  .headline {
    position: absolute; left: 22px; color: var(--headline);
    font: 400 42px/43px "Questrial", sans-serif; letter-spacing: 1px;
    text-shadow: 0 2px 3px rgba(0,0,0,.35);
  }
  .banner-1 .headline { left: 24px; top: 64px; font-size: 38px; line-height: 42px; z-index: 1; }
  .banner-2 .headline, .banner-3 .headline { top: 18px; }
  .body-copy {
    position: absolute; left: 22px; top: 114px; width: 300px;
    color: var(--headline); font: 16.5px/24px "Open Sans", sans-serif;
  }
  .cta {
    position: absolute; left: 16px; top: 259px; z-index: 2;
    display: flex; align-items: center; gap: 8px;
    color: var(--ink); font: 700 22px/1 "Open Sans", sans-serif;
  }
  .cta svg { width: 21px; height: 21px; }
  .mascot-area {
    position: absolute; left: 214px; top: 74px; width: 140px; height: 214px;
    border-radius: 60px 60px 24px 24px;
    background: linear-gradient(180deg, var(--mascot-mid), var(--mascot-dark));
  }
  .people-area {
    position: absolute; left: 246px; top: 193px; width: 102px; height: 70px;
    border-radius: 8px;
    background: linear-gradient(180deg, var(--figure-grey), rgba(217,217,217,.25));
  }
  .dollar-area {
    position: absolute; left: 250px; top: 150px; width: 106px; height: 142px;
    border-radius: 24px;
    background: linear-gradient(135deg, var(--coin-silver), var(--coin-shadow));
  }
  .bar-chart { position: absolute; left: 178px; top: 178px; }
</style>
</head>
<body>
<main class="board">
  <h1 class="format-title">300x250</h1>

  <svg width="0" height="0" style="position:absolute">
    <defs>
      <linearGradient id="redGlow" x1="0" y1="0" x2="1" y2="1">
        <stop offset="0" stop-color="#b8150d"/>
        <stop offset="1" stop-color="#9a0a05"/>
      </linearGradient>
      <linearGradient id="bandFade" x1="0" y1="0" x2="1" y2="0">
        <stop offset="0" stop-color="#ffffff"/>
        <stop offset="0.6" stop-color="#f6eeee"/>
        <stop offset="1" stop-color="#e6d2d2"/>
      </linearGradient>
      <symbol id="bannerBg" viewBox="0 0 360 300">
        <rect width="360" height="300" fill="url(#redGlow)"/>
        <path d="M0 190 C100 224 220 238 360 236 L360 300 L0 300 Z" fill="#6e0603"/>
        <path d="M0 206 C100 236 220 252 360 252 L360 300 L0 300 Z" fill="url(#bandFade)"/>
      </symbol>
      <symbol id="signupIcon" viewBox="0 0 21 21">
        <rect x="1.5" y="1.5" width="18" height="18" rx="5" fill="none" stroke="#1c1c1c" stroke-width="2.2"/>
        <path d="M10.5 16 V6 M6.5 10 L10.5 6 L14.5 10" fill="none" stroke="#1c1c1c" stroke-width="2.2" stroke-linecap="round" stroke-linejoin="round"/>
      </symbol>
    </defs>
  </svg>

  <section class="banner banner-1">
    <svg class="banner-bg" viewBox="0 0 360 300"><use href="#bannerBg"/></svg>
    <p class="kicker">Keep Control of your</p>
    <h2 class="headline">WEBSITE<br>TRAFFIC</h2>
    <div class="mascot-area" role="img" aria-label="Cartoon mascot in a dark suit and sunglasses holding a cigar"></div>
    <a class="cta"><svg><use href="#signupIcon"/></svg>Signup Today</a>
  </section>
  <p class="frame-label" style="left:205px; top:645px;">Frame1</p>

  <section class="banner banner-2">
    <svg class="banner-bg" viewBox="0 0 360 300"><use href="#bannerBg"/></svg>
    <h2 class="headline">BUY TRAFFIC<br>ADVERTISE</h2>
    <p class="body-copy">You think that Searchly AdPlacer advertising is way too expensive? We do too!</p>
    <svg class="bar-chart" width="60" height="72" viewBox="0 0 60 72" aria-label="Rising bar chart">
      <rect x="0" y="50" width="7" height="22" fill="var(--chart-white)"/>
      <rect x="12" y="38" width="7" height="34" fill="var(--chart-white)"/>
      <rect x="24" y="26" width="7" height="46" fill="var(--chart-white)"/>
      <rect x="36" y="14" width="7" height="58" fill="var(--chart-white)"/>
      <rect x="48" y="0" width="7" height="72" fill="var(--chart-white)"/>
    </svg>
    <div class="people-area" role="img" aria-label="Three grey person figures with reflections"></div>
    <a class="cta"><svg><use href="#signupIcon"/></svg>Signup Today</a>
  </section>
  <p class="frame-label" style="left:613px; top:645px;">Frame2</p>

  <section class="banner banner-3">
    <svg class="banner-bg" viewBox="0 0 360 300"><use href="#bannerBg"/></svg>
    <h2 class="headline">SELL TRAFFIC<br>MONETISE</h2>
    <p class="body-copy">Would you like to generate some revenue with your traffic?</p>
    <div class="dollar-area" role="img" aria-label="Large silver 3D dollar sign"></div>
    <a class="cta"><svg><use href="#signupIcon"/></svg>Signup Today</a>
  </section>
  <p class="frame-label" style="left:1030px; top:636px;">Frame3</p>
</main>
</body>
</html>
```